Entertainer/Dancer Business Cards

Devon Marsh is an up and coming entertainer from Baltimore, Maryland currently relocating to Los Angeles, California for a dance opportunity at the renowned Ruthie Calder Dance Studio.
This young man needs to promote himself and his skills in a populous and competitive city.
Hopefully, this card will set him apart from the tons of entertainers in L.A.
It will passed out to fellow entertainers, agents, and random people looking for talent.

I have uploaded an image of the dancer, it is not necessary to use this image; however it is in PSD format if one should decide to incorporate it somehow and would like to make changes.

Industry/Entity Type

Business

Contact Information for Business Card

Devon Marsh
(line 1) Dancer Choreographer Instructor Singer/Songwriter
(line 2) Ballet-Modern-Urban
devonmarsh00@fernpost.com
410-582-7146

Requirements
Nice to have

• Open to an all typography card.
Should not have
• No logo; just name: Devon Marsh
Devon is a guy (in case you were wondering :D )
Please no ballet/pointe shoes in design

```html
<!DOCTYPE html>
<html lang="en">
<head>
<meta charset="utf-8">
<title>Devon Marsh — Business Card</title>
<link rel="stylesheet" href="https://fonts.googleapis.com/css2?family=Arimo:wght@400;700&display=swap">
<style>
  :root {
    --page: #e9eaec;
    --navy: #22345a;
    --navy-deep: #1b2a4a;
    --band: #fafafa;
    --accent: #c9662a;
    --portrait-light: #3a66b4;
    --portrait-mid: #2a4f9a;
    --portrait-dark: #1e3a76;
  }
  html, body {
    margin: 0;
    width: 1200px;
    height: 1000px;
    overflow: hidden;
    background: var(--page);
  }
  .canvas {
    position: relative;
    width: 1200px;
    height: 1000px;
  }
  .business-card {
    position: absolute;
    left: 75px;
    top: 200px;
    width: 1050px;
    height: 600px;
    box-shadow: 0 14px 36px rgba(0,0,0,0.22);
  }
  .business-card svg { display: block; }
  .card-text { font-family: "Arimo", Arial, sans-serif; fill: var(--accent); }
  .card-name { font-size: 44px; font-weight: 700; }
  .card-line { font-size: 21px; font-weight: 400; }
  .card-contact { font-size: 24px; font-weight: 700; }
</style>
</head>
<body>
<div class="canvas">
  <div class="business-card">
    <svg width="1050" height="600" viewBox="0 0 1050 600" xmlns="http://www.w3.org/2000/svg">
      <defs>
        <radialGradient id="portrait-tones" cx="0.5" cy="0.4" r="0.65">
          <stop offset="0" stop-color="var(--portrait-light)"/>
          <stop offset="0.6" stop-color="var(--portrait-mid)"/>
          <stop offset="1" stop-color="var(--portrait-dark)"/>
        </radialGradient>
      </defs>

      <rect class="card-ground" width="1050" height="600" fill="var(--navy)"/>

      <polygon class="diagonal-band" points="0,370 720,0 1010,0 860,130 620,436 300,600 0,600" fill="var(--band)"/>

      <circle class="portrait-ring" cx="790" cy="275" r="240" fill="var(--navy-deep)"/>
      <circle class="portrait" cx="790" cy="275" r="212" fill="url(#portrait-tones)"
              role="img" aria-label="Photo of the dancer in an extended leg pose on a harbour pier at night"/>

      <g class="card-text" transform="translate(40 440) rotate(-27)">
        <text class="card-name" x="0" y="0">Devon Marsh</text>
        <line class="name-rule" x1="0" y1="12" x2="330" y2="12" stroke="var(--accent)" stroke-width="2"/>
        <text class="card-line" x="0" y="45">Dancer Choreographer Instructor Singer/Songwriter</text>
        <text class="card-line" x="0" y="75">Ballet-Modern-Urban</text>
        <text class="card-contact" x="0" y="110">devonmarsh00@fernpost.com</text>
        <text class="card-contact" x="0" y="140">410-582-7146</text>
      </g>
    </svg>
  </div>
</div>
</body>
</html>
```